Poster design for Chattanooga, TN's 175th Anniversary. Here is a link to our website www.lmw482.org.

Basically, this is a weeklong celebration of community-sourced events highlighting mostly our city's past. Pellworth Tilly Tram (railroads) are big in our past, and we are identified by our river and surrounded by mountains. The week will have a variety of different events so we need to drive people to our website as events will be added continually.

Also, this event is being put on by our local Mayor's office. While we are young and progressive, can't be too crazy or out there. I was thinking more like a throwback concert photo, a la Brindle Loft Presses (famous in Nashville). That would help tie in the vintage vibe.

Reason: I need to provide my comm team with designs next week. This will give everyone the weekend to be creative!

Target Market(s)

Local Chattanooga Residents - kids, young people, older people.

Requirements
Must have
• (website) LMW482.org
• (Date) November 8 - November 15, 2014
Nice to have
• Flag (doesn't matter the treatment)
• "Weeklong Celebration"
• "Community-Sourced Events"
• Logo (doesn't matter the treatment)
• 175 years of Chattanooga
• Stars
Should not have
• any kind of vulgar image or language.
• Should not be pink or purple or neon.

```html
<!DOCTYPE html>
<html lang="en">
<head>
<meta charset="utf-8">
<title>Chattanooga 175 Anniversary Poster</title>
<link href="https://fonts.googleapis.com/css2?family=Anton&family=Arvo:wght@700&display=swap" rel="stylesheet">
<style>
  :root {
    --paper: #c7c7c5;
    --paper-light: #d3d3d1;
    --teal: #2f8b9b;
    --teal-light: #45a0ae;
    --teal-deep: #1e6f80;
    --ink: #3f3f3f;
    --ink-dots: #555555;
    --white: #f2f2f2;
    --title-letter: #d0d0ce;
    --photo-sky: #3b3b55;
    --photo-red: #9a2a1c;
    --photo-ground: #5a4320;
  }
  html, body {
    margin: 0;
    padding: 0;
    overflow: hidden;
    background: #ffffff;
  }
  .poster {
    position: relative;
    width: 848px;
    height: 1200px;
    overflow: hidden;
    background: radial-gradient(ellipse at 40% 30%, var(--paper-light), var(--paper) 70%);
    font-family: "Arvo", Georgia, serif;
  }
  .header {
    position: absolute;
    left: 0;
    top: 0;
  }
  .title-word {
    font-family: "Anton", "Arial Narrow", sans-serif;
    font-size: 250px;
    fill: var(--title-letter);
  }
  .ribbon-text {
    font-family: "Arvo", Georgia, serif;
    font-weight: 700;
    font-size: 20px;
    fill: var(--white);
    letter-spacing: 0.5px;
  }
  .dot-row {
    position: absolute;
    height: 12px;
    background-image: radial-gradient(circle, var(--ink-dots) 5px, transparent 5.5px);
    background-size: 15px 12px;
    background-repeat: repeat-x;
  }
  .dot-row.under-header { left: 234px; top: 402px; width: 372px; }
  .dot-row.footer { left: 34px; top: 1128px; width: 796px; }
  .scene-image {
    position: absolute;
    left: 0;
    top: 426px;
    width: 848px;
    height: 390px;
    background:
      radial-gradient(ellipse at 48% 55%, var(--photo-red) 0%, rgba(154,42,28,0.6) 25%, transparent 50%),
      linear-gradient(180deg, var(--photo-sky) 0%, #2e2a2e 45%, var(--photo-ground) 100%);
  }
  .features {
    position: absolute;
    left: 30px;
    top: 840px;
    margin: 0;
    padding: 0 0 0 20px;
    list-style: none;
    border-left: 3px dotted var(--ink);
  }
  .features li {
    position: relative;
    font-weight: 700;
    font-size: 30px;
    line-height: 56px;
    color: var(--ink);
  }
  .features li::before {
    content: "";
    position: absolute;
    left: -27px;
    top: 23px;
    width: 11px;
    height: 11px;
    border-radius: 50%;
    background: var(--ink);
  }
  .pointer {
    position: absolute;
    left: 222px;
    top: 872px;
  }
  .date-box {
    position: absolute;
    left: 486px;
    top: 828px;
    width: 336px;
    height: 248px;
    box-sizing: border-box;
    border: 4px dotted var(--ink);
    color: var(--teal-deep);
    text-align: center;
    font-weight: 700;
  }
  .date-days { font-size: 72px; line-height: 1; margin-top: 30px; letter-spacing: 3px; }
  .date-month { font-size: 38px; line-height: 1; margin-top: 8px; letter-spacing: 1px; }
  .date-year { font-size: 88px; line-height: 1; margin-top: 4px; letter-spacing: 3px; }
  .website {
    position: absolute;
    left: 0;
    top: 1086px;
    width: 848px;
    text-align: center;
    font-weight: 700;
    font-size: 22px;
    letter-spacing: 1px;
    color: var(--teal-deep);
  }
</style>
</head>
<body>
<main class="poster">
  <svg class="header" width="848" height="420" viewBox="0 0 848 420">
    <defs>
      <clipPath id="banner-shape">
        <path d="M30 30 H818 V414 H790 Q424 30 58 414 H30 Z"/>
      </clipPath>
    </defs>
    <path class="title-banner" d="M30 30 H818 V414 H790 Q424 30 58 414 H30 Z" fill="var(--teal)"/>
    <g clip-path="url(#banner-shape)">
      <text class="title-word" x="424" y="252" text-anchor="middle" textLength="740" lengthAdjust="spacingAndGlyphs">CHATTANOOGA</text>
    </g>
    <path class="anniversary-ribbon" d="M222 292 Q424 206 626 292 V378 H222 Z" fill="var(--teal)"/>
    <line x1="332" y1="272" x2="516" y2="272" stroke="var(--white)" stroke-width="4" stroke-dasharray="0 9" stroke-linecap="round"/>
    <line x1="262" y1="302" x2="586" y2="302" stroke="var(--white)" stroke-width="1.5"/>
    <text class="ribbon-text" x="424" y="329" text-anchor="middle">TN's 175 ANNIVERSARY</text>
    <line x1="262" y1="344" x2="586" y2="344" stroke="var(--white)" stroke-width="1.5"/>
    <line x1="352" y1="360" x2="496" y2="360" stroke="var(--white)" stroke-width="3" stroke-dasharray="0 8" stroke-linecap="round"/>
    <g fill="var(--teal)" stroke="var(--white)" stroke-width="2">
      <polygon points="198,290 209,320 241,320 215,339 225,370 198,351 171,370 181,339 155,320 187,320"/>
      <polygon points="650,290 661,320 693,320 667,339 677,370 650,351 623,370 633,339 607,320 639,320"/>
      <polygon points="130,340 136,354 151,354 139,363 143,378 130,369 117,378 121,363 109,354 124,354"/>
      <polygon points="718,340 724,354 739,354 727,363 731,378 718,369 705,378 709,363 697,354 712,354"/>
      <polygon points="84,374 89,385 101,385 91,392 95,404 84,397 73,404 77,392 67,385 79,385"/>
      <polygon points="764,374 769,385 781,385 771,392 775,404 764,397 753,404 757,392 747,385 759,385"/>
    </g>
    <g fill="var(--white)">
      <polygon points="346,354 348,359 353,359 349,362 351,367 346,364 341,367 343,362 339,359 344,359"/>
      <polygon points="502,354 504,359 509,359 505,362 507,367 502,364 497,367 499,362 495,359 500,359"/>
    </g>
  </svg>

  <div class="dot-row under-header"></div>

  <div class="scene-image" role="img" aria-label="Painted illustration of a vintage steam locomotive with a red cowcatcher and holiday wreath at a lit-up station at night"></div>

  <ul class="features">
    <li>Music</li>
    <li>Sport</li>
    <li>Artful Shop</li>
    <li>Local 191 Cocktail</li>
  </ul>

  <svg class="pointer" width="214" height="56" viewBox="0 0 214 56" aria-hidden="true">
    <line x1="0" y1="28" x2="112" y2="28" stroke="var(--ink)" stroke-width="3" stroke-dasharray="2 3"/>
    <polygon points="120,18 166,18 166,2 212,28 166,54 166,38 120,38" fill="var(--ink)"/>
  </svg>

  <div class="date-box">
    <div class="date-days">08-15</div>
    <div class="date-month">NOVEMBER</div>
    <div class="date-year">2014</div>
  </div>

  <p class="website" style="margin:0">www.lmw482.org</p>

  <div class="dot-row footer"></div>
</main>
</body>
</html>
```